Mortgage Protection Insurance Flyer

The target audience are new home owners so the design needs to be clean and simple.

This a primarily for Final Expense Insurance, but need an area where it says "We Also Specialize In:"
- Medicare Supplement Insurance (MediGap)
- Annuities
- Final Expense

All flyer versions need to be editable. Colors to be used are red, white or black. Refer to my website for colors and photos (harborvaleassurance.com). Will attach my logo and a flyer that I found online that is the format that I am looking for (for 8.5 in. x 11 in version). Need flyer in standard letter size 8.5 in. x11 in. but also in 8.5 in. x 5.5 in and 5.0 in. x 8.0 in. All sizes to be portrait oriented. If picked as winning design, need all flyer versions in full color, also in grey scale and files in all industry file types.

Content can be taken from my website..... harborvaleassurance.com

Do NOT submit if you are not willing to provide all versions as described above for the original project price.

Must use royalty-free stock photos please.

Target Market(s)

New homeowners looking for insurance to protect there mortgage payments

Industry/Entity Type

Life Insurance

Colors
f69fa3

Requirements
Must have
• Colors to be used are red, white or black.
• Need flyer in standard letter size 8.5 in. x11 in. but also in 3.5 in. x 8.5 in (Full Bleed 3.75 in by 8.75 in.) and 4.0 in. x 6.0 in. (Full Bleed 4.12 in x 6.12 in) Each design tailored to the size dimensions (So no squeezing 8.5 x 11 design into a 4.0 x 6.0 space.) All sizes to be portrait oriented. If picked as winning design, need all flyer versions in full color, also in grey scale and files in all file types.
• Do not need physical address on flyer, do need email address on flyer though - tkerlow@harborvaleassurance.com
• So phone number should be prominent, email address and website address should also be contact area.
• If you can not agree to terms above, do not submit any designs.
• Need facebook & twitter logos somewhere in contact info area.
Nice to have
• See sample flyers I have attached.
• White background with red used as primary graphic color and black used as secondary graphic if needed.
• font to be used should similar to one used in logo.

```html
<!DOCTYPE html>
<html lang="en">
<head>
<meta charset="utf-8">
<title>Harborvale Assurance – Final Expense Flyer</title>
<link rel="stylesheet" href="https://fonts.googleapis.com/css2?family=Montserrat:wght@400;500;600;700;800&family=Roboto+Condensed:ital,wght@1,800&display=swap">
<style>
:root{
  --red:#d3151c;
  --red-bright:#e3242b;
  --ink:#231f20;
  --text:#3a3a3a;
  --paper:#f3f3f3;
  --stage:#4a4a4a;
  --grey-cell:#dcdcdc;
}
*{margin:0;padding:0;box-sizing:border-box}
html,body{width:1200px;height:857px;overflow:hidden;background:var(--stage)}
.flyer{position:absolute;left:295px;top:19px;width:610px;height:818px;background:var(--paper);overflow:hidden;font-family:'Montserrat',sans-serif;color:var(--text)}
.hero-photo{position:absolute;left:290px;top:0;width:320px;height:340px;background:linear-gradient(160deg,#e9e9e9 0%,#c9c9c9 45%,#9a9a9a 75%,#d8d8d8 100%)}
.wave{position:absolute;left:0;top:0;width:610px;height:818px}
.brand{position:absolute;left:33px;top:58px;font-weight:800;font-size:25px;letter-spacing:1px;color:var(--ink);line-height:1}
.brand-dot{display:inline-block;width:10px;height:10px;background:var(--red);border-radius:50%;margin-left:6px;vertical-align:middle}
.headline{position:absolute;left:31px;top:128px;font-family:'Roboto Condensed',sans-serif;font-style:italic;font-weight:800;font-size:39px;line-height:41px;color:var(--ink);text-transform:uppercase}
.headline em{color:var(--red-bright);font-style:italic}
.intro{position:absolute;left:31px;top:329px;width:248px;font-size:9.6px;line-height:12.4px;text-align:justify}
.rates{position:absolute;left:31px;top:388px;width:248px}
.rate{display:flex;height:20px;margin-bottom:3px;font-size:9.6px}
.rate-label{width:162px;background:var(--grey-cell);padding-left:11px;line-height:20px;font-weight:500}
.rate-value{flex:1;margin-left:2px;background:var(--red-bright);color:#fff;font-weight:700;text-align:center;line-height:20px;border-radius:2px}
.section-title{position:absolute;left:31px;font-weight:700;font-size:11px;color:var(--ink)}
.checklist{list-style:none}
.checklist li{position:relative;padding-left:15px;font-size:9.6px;line-height:16.5px}
.checklist svg{position:absolute;left:0;top:4px;width:8px;height:8px}
.specialties{position:absolute;left:31px;top:474px}
.body-copy{position:absolute;left:31px;width:257px;font-size:9.6px;line-height:12.5px;text-align:justify}
.panel{position:absolute;left:311px;top:322px;width:267px;height:365px;background:var(--red);border-radius:0 0 12px 12px;color:#fff;box-shadow:0 6px 8px -6px rgba(0,0,0,.45)}
.panel-tab{position:absolute;left:-5px;height:20px;background:var(--ink);color:#fff;font-weight:700;font-size:10.5px;line-height:20px;padding:0 14px 0 23px;border-radius:0 10px 10px 0}
.panel-copy{position:absolute;left:19px;top:76px;width:231px;font-size:9.4px;line-height:11.8px;text-align:justify}
.benefits{position:absolute;left:19px;top:183px;width:231px}
.benefits li{font-size:9.4px;line-height:11.8px;margin-bottom:6.8px;padding-left:15px;text-align:justify}
.benefits svg{top:2px}
.fine-print{position:absolute;left:316px;top:717px;width:259px;font-size:8.6px;line-height:11px;text-align:justify}
.footer-bar{position:absolute;left:0;top:774px;width:610px;height:36px;background:var(--ink)}
.footer-line{position:absolute;left:0;top:812px;width:610px;height:6px;background:var(--red)}
.footer-phone{position:absolute;left:0;top:769px;width:214px;height:49px;background:var(--red);border-top-right-radius:30px;display:flex;align-items:center;padding-left:31px;color:#fff;font-weight:700;font-size:16px}
.footer-phone svg{width:14px;height:14px;margin-right:9px}
.contact{position:absolute;top:785px;display:flex;align-items:center;color:#fff;font-size:8.8px}
.contact svg{width:9px;height:9px;margin-right:8px}
.social{position:absolute;top:784px;left:546px;display:flex;gap:8px}
.social span{width:13px;height:13px;border-radius:50%;background:#fff}
</style>
</head>
<body>
<main class="flyer">
  <div class="hero-photo" role="img" aria-label="Photo of a smiling senior couple embracing in a bright home"></div>

  <svg class="wave" viewBox="0 0 610 818" aria-hidden="true">
    <path d="M0,318 C120,280 250,280 360,318 C440,345 530,338 610,302 L610,818 L0,818 Z" fill="#f3f3f3"/>
    <path d="M0,300 C120,262 250,262 360,300 C440,328 530,322 610,282 L610,300 C530,338 440,345 360,318 C250,282 120,282 0,318 Z" fill="#e3242b"/>
    <path d="M220,276 C280,272 330,285 380,303 C450,328 530,320 610,282 L610,290 C530,330 450,336 380,312 C330,294 280,280 220,276 Z" fill="#231f20"/>
  </svg>

  <div class="brand">HARBORVALE ASSURANCE<span class="brand-dot"></span></div>

  <h1 class="headline">Our <em>Plans Are</em><br>Based On Yours</h1>

  <p class="intro">Get the right Final Expense Insurance, Medicare Supplement Insurance or Mortgage Protection Insurance plan for your family's peace-of-mind!</p>

  <div class="rates">
    <div class="rate"><span class="rate-label">Monthly premiums as low as</span><span class="rate-value">$10</span></div>
    <div class="rate"><span class="rate-label">Death Benefits as high as</span><span class="rate-value">$40,000</span></div>
  </div>

  <h2 class="section-title" style="top:453px">We Also Specialize In:</h2>
  <ul class="checklist specialties">
    <li><svg viewBox="0 0 10 10"><rect x="0.5" y="1.5" width="8" height="8" fill="none" stroke="#e3242b" stroke-width="1.2"/><path d="M2.5,5 L4.5,7 L9.5,1" fill="none" stroke="#e3242b" stroke-width="1.5"/></svg>Medicare Supplement Insurance (MediGap)</li>
    <li><svg viewBox="0 0 10 10"><rect x="0.5" y="1.5" width="8" height="8" fill="none" stroke="#e3242b" stroke-width="1.2"/><path d="M2.5,5 L4.5,7 L9.5,1" fill="none" stroke="#e3242b" stroke-width="1.5"/></svg>Annuities</li>
    <li><svg viewBox="0 0 10 10"><rect x="0.5" y="1.5" width="8" height="8" fill="none" stroke="#e3242b" stroke-width="1.2"/><path d="M2.5,5 L4.5,7 L9.5,1" fill="none" stroke="#e3242b" stroke-width="1.5"/></svg>Mortgage Protection Insurance</li>
  </ul>

  <h2 class="section-title" style="top:537px">Assessing Need</h2>
  <p class="body-copy" style="top:556px">Unforeseen events and a lack of the right kind of insurance can spell trouble quickly. Contact us today, to set up a free assessment time. We will analyze your insurance needs and get you and your family the right coverage quickly at a budget friendly price.</p>

  <h2 class="section-title" style="top:644px">Your Unique</h2>
  <p class="body-copy" style="top:663px;text-align:left">Everyone has different insurance needs.<br>Find out how we can give you the peace of mind knowing your family wont have a financial burden if something were to happen to you.</p>
  <p class="body-copy" style="top:725px;text-align:left">Find out how we can help find the right plan to keep your medical costs manageable.</p>

  <section class="panel">
    <div class="panel-tab" style="top:44px">Final Expense Insurance</div>
    <p class="panel-copy">Final Expense Insurance is a type of permanent life insurance where the death benefit is used to cover (but not limited to) medical costs, funeral costs and other end-of-life expenses. It is a budget friendly option with a death benefit of up to $40k.</p>
    <div class="panel-tab" style="top:155px">Benefits</div>
    <ul class="checklist benefits">
      <li><svg viewBox="0 0 10 10"><rect x="0.5" y="1.5" width="8" height="8" fill="none" stroke="#fff" stroke-width="1.2"/><path d="M2.5,5 L4.5,7 L9.5,1" fill="none" stroke="#fff" stroke-width="1.5"/></svg>All plans we offer are state regulated</li>
      <li><svg viewBox="0 0 10 10"><rect x="0.5" y="1.5" width="8" height="8" fill="none" stroke="#fff" stroke-width="1.2"/><path d="M2.5,5 L4.5,7 L9.5,1" fill="none" stroke="#fff" stroke-width="1.5"/></svg>Relatively low monthly premiums</li>
      <li><svg viewBox="0 0 10 10"><rect x="0.5" y="1.5" width="8" height="8" fill="none" stroke="#fff" stroke-width="1.2"/><path d="M2.5,5 L4.5,7 L9.5,1" fill="none" stroke="#fff" stroke-width="1.5"/></svg>Premiums can never increase</li>
      <li><svg viewBox="0 0 10 10"><rect x="0.5" y="1.5" width="8" height="8" fill="none" stroke="#fff" stroke-width="1.2"/><path d="M2.5,5 L4.5,7 L9.5,1" fill="none" stroke="#fff" stroke-width="1.5"/></svg>Your policy can never be cancelled as long as you pay your premium</li>
      <li><svg viewBox="0 0 10 10"><rect x="0.5" y="1.5" width="8" height="8" fill="none" stroke="#fff" stroke-width="1.2"/><path d="M2.5,5 L4.5,7 L9.5,1" fill="none" stroke="#fff" stroke-width="1.5"/></svg>No medical exams</li>
      <li><svg viewBox="0 0 10 10"><rect x="0.5" y="1.5" width="8" height="8" fill="none" stroke="#fff" stroke-width="1.2"/><path d="M2.5,5 L4.5,7 L9.5,1" fill="none" stroke="#fff" stroke-width="1.5"/></svg>Guaranteed Death Benefit</li>
      <li><svg viewBox="0 0 10 10"><rect x="0.5" y="1.5" width="8" height="8" fill="none" stroke="#fff" stroke-width="1.2"/><path d="M2.5,5 L4.5,7 L9.5,1" fill="none" stroke="#fff" stroke-width="1.5"/></svg>Many policies we offer are Guaranteed Acceptance, "Day 1" coverage, have a child/grandchild rider &amp;/or have an accelerated death benefit rider</li>
    </ul>
  </section>

  <p class="fine-print">Based on an insured that is a 65 year old, non-smoking female that has no medical conditions with death benefit of $2k</p>

  <div class="footer-bar"></div>
  <div class="footer-line"></div>
  <div class="footer-phone">
    <svg viewBox="0 0 24 24"><path d="M6.6 10.8a15.2 15.2 0 0 0 6.6 6.6l2.2-2.2a1 1 0 0 1 1-.25 11.4 11.4 0 0 0 3.6.57 1 1 0 0 1 1 1V20a1 1 0 0 1-1 1A17 17 0 0 1 3 4a1 1 0 0 1 1-1h3.5a1 1 0 0 1 1 1c0 1.25.2 2.45.57 3.57a1 1 0 0 1-.25 1z" fill="#fff"/></svg>
    (555)014.2687
  </div>
  <div class="contact" style="left:219px">
    <svg viewBox="0 0 10 10"><rect x="0.5" y="2" width="9" height="7" rx="1" fill="#e3242b"/><path d="M0.5,2.5 L5,6 L9.5,2.5" fill="none" stroke="#231f20" stroke-width="1"/></svg>
    tkerlow@harborvaleassurance.com
  </div>
  <div class="contact" style="left:389px">
    <svg viewBox="0 0 10 10"><circle cx="5" cy="5" r="4.3" fill="none" stroke="#e3242b" stroke-width="1.2"/><path d="M0.7,5 H9.3 M5,0.7 C2.5,3 2.5,7 5,9.3 M5,0.7 C7.5,3 7.5,7 5,9.3" fill="none" stroke="#e3242b" stroke-width="0.9"/></svg>
    www.harborvaleassurance.com
  </div>
  <div class="social" aria-label="Social media"><span></span><span></span></div>
</main>
</body>
</html>
```